Business Card Design Z9 MOTORS

Hi firstly I would like you to design a professional logo for my company. By using words " Z9 Auto Spares & Haulage".
We are an auto dismantling company where we buy wrecks/cars for dismantling and selling salvageable parts again.

Hi every one,

Thank you for posting the designs. But unfortunately non of these designs have the logo that I would prefer for my company. I will be branding the logo quite extensively, therefore please design some professional looking ones.

Thanks

Industry/Entity Type

Business

Contact Information for Business Card

Z9 Auto Spares & Haulage, 472 Kowhai Bend Rd, Fernmoor, Wellington
T: 04 7261048, F: 04 7261049, E: dean.morrow@z9motors.example.nz, W: www.z9motors.example.nz
Name: Dean L Morrow
Managing Director
Mob: 027418906

At the bottom of card " WE PAY TOP $$$$ FOR ANY UNWANTED VEHICLES FOR FOR DISMANTLING CALL US NOW 0800372815"

```html
<!DOCTYPE html>
<html lang="en">
<head>
<meta charset="utf-8">
<title>Z9 Motors – Business Card</title>
<link href="https://fonts.googleapis.com/css2?family=Arimo:ital,wght@0,400;0,700;1,400&display=swap" rel="stylesheet">
<style>
  :root {
    --bg-top: #eef1f1;
    --bg-mid: #dfe5e6;
    --bg-low: #cfd9da;
    --ink: #1a1a1a;
    --stripe-black: #0d0d0d;
    --stripe-red: #e30613;
    --brand-red: #c5101a;
  }
  html, body {
    margin: 0;
    padding: 0;
    overflow: hidden;
    background: #ffffff;
  }
  .card {
    position: relative;
    width: 1200px;
    height: 741px;
    overflow: hidden;
    font-family: "Arimo", Arial, sans-serif;
    color: var(--ink);
    background: linear-gradient(180deg, var(--bg-top) 0%, var(--bg-mid) 44%, var(--bg-low) 46%, #d6dfe0 100%);
  }
  .card__stripes {
    position: absolute;
    inset: 0;
  }
  .holder-name {
    position: absolute;
    left: 63px;
    top: 252px;
    margin: 0;
    font-size: 53px;
    font-weight: 400;
    letter-spacing: 0.5px;
  }
  .holder-rule {
    position: absolute;
    left: 65px;
    top: 313px;
    width: 472px;
    height: 2px;
    background: var(--ink);
  }
  .holder-title {
    position: absolute;
    right: 683px;
    top: 316px;
    margin: 0;
    font-size: 35px;
    font-style: italic;
  }
  .holder-contact {
    position: absolute;
    left: 59px;
    top: 384px;
    margin: 0;
    font-size: 28px;
    line-height: 41px;
  }
  .offer {
    position: absolute;
    left: 30px;
    width: 556px;
    top: 626px;
    margin: 0;
    text-align: center;
    font-size: 19.5px;
    line-height: 30px;
    text-transform: uppercase;
  }
  .brand-name {
    position: absolute;
    left: 700px;
    width: 460px;
    top: 300px;
    margin: 0;
    text-align: center;
    font-size: 76px;
    font-weight: 700;
    color: var(--brand-red);
    letter-spacing: 1px;
  }
  .company-rule {
    position: absolute;
    left: 676px;
    top: 518px;
    width: 470px;
    height: 2px;
    background: var(--ink);
  }
  .company-details {
    position: absolute;
    right: 70px;
    top: 550px;
    margin: 0;
    text-align: right;
    font-size: 23px;
    line-height: 35px;
    font-weight: 700;
  }
</style>
</head>
<body>
  <div class="card">
    <svg class="card__stripes" width="1200" height="741" viewBox="0 0 1200 741" aria-hidden="true">
      <polygon points="746,0 789,0 683,357" fill="var(--stripe-black)"/>
      <polygon points="683,368 546,741 508,741" fill="var(--stripe-red)"/>
    </svg>

    <h1 class="holder-name">Dean L. Morrow</h1>
    <div class="holder-rule"></div>
    <p class="holder-title">Managing Director</p>
    <p class="holder-contact">
      mob.: 027418906<br>
      email: dean.morrow@z9motors.example.nz
    </p>

    <p class="offer">
      We pay top $$$$ for any unwanted vehicles<br>
      for dismantling call us now 0800372815
    </p>

    <p class="brand-name">Z9 MOTORS</p>
    <div class="company-rule"></div>
    <p class="company-details">
      Z9 Auto Spares &amp; Haulage<br>
      472 Kowhai Bend Rd, Fernmoor, Wellington<br>
      Tel. No.:&nbsp; 04 7261048 : Fax No.:04 7261049
    </p>
  </div>
</body>
</html>
```